Award-winnning Estate Agent needs a premium version of their 'For Sale' board design

We need a premium option for our 'For Sale' board design. We have a standard board that is attached to this brief, but were are looking to have a premium design version that we will use when selling exclusive properties. Our company name is Harbour Lane Estates and the name for this is exclusive selection is: 'The Harbour Collection'. The design needs to work with our current brand, but have a distinctive PREMIUM feel to it. I have uploaded the barnd guidelines and also some of the exisisting logo variations. We do NOT need a new logo but feel free to play around with colours, fonts, sizes etc. for the sign.

Target Market(s)

Property buyers & house hunters

Industry/Entity Type

Real Estate - Residential Property

Font styles to use
Sans Serif

Requirements
Must have
• A premium fee, must be square design, must be easy to read when driving past the sign
Nice to have
• I'm open ot ideas

```html
<!DOCTYPE html>
<html lang="en">
<head>
<meta charset="utf-8">
<title>Harbour Lane Estates – The Harbour Collection For Sale Board</title>
<link rel="stylesheet" href="https://fonts.googleapis.com/css2?family=Arimo:wght@400;700&display=swap">
<style>
  :root {
    --premium-navy: #26225f;
    --brand-navy: #3a3483;
    --brand-blue: #2b73b9;
    --sky-blue: #2eaae2;
    --accent-gold: #c9a75a;
    --board-white: #ffffff;
    --ink: #1d1d1f;
    --backdrop: #e8e8ea;
  }
  * { margin: 0; padding: 0; box-sizing: border-box; }
  html, body {
    width: 916px;
    height: 1200px;
    overflow: hidden;
    background: var(--backdrop);
  }
  .canvas {
    width: 916px;
    height: 1200px;
    display: flex;
    align-items: center;
    justify-content: center;
  }
  .sale-board {
    width: 820px;
    height: 820px;
    display: block;
    background: var(--board-white);
    box-shadow: 0 6px 24px rgba(0, 0, 0, 0.14);
    font-family: "Arimo", Arial, sans-serif;
  }
  .board-band { fill: var(--premium-navy); }
  .band-edge {
    fill: none;
    stroke: var(--accent-gold);
    stroke-width: 5;
  }
  .board-frame {
    fill: none;
    stroke: var(--accent-gold);
    stroke-width: 4;
  }
  .board-headline {
    fill: var(--board-white);
    font-weight: 700;
    font-size: 118px;
    letter-spacing: 3px;
  }
  .collection-name {
    fill: var(--accent-gold);
    font-weight: 700;
    font-size: 25px;
    letter-spacing: 6px;
  }
  .brand-square { fill: var(--brand-blue); }
  .brand-name {
    fill: var(--brand-navy);
    font-weight: 700;
    font-size: 54px;
  }
  .phone-pill { fill: var(--premium-navy); }
  .phone-badge { fill: var(--board-white); }
  .phone-handset { fill: var(--sky-blue); }
  .phone-number {
    fill: var(--board-white);
    font-weight: 700;
    font-size: 60px;
    letter-spacing: 1px;
  }
  .web-address {
    font-weight: 400;
    font-size: 34px;
    fill: var(--ink);
  }
  .web-address .web-domain { fill: var(--brand-blue); }
</style>
</head>
<body>
<main class="canvas">
  <svg class="sale-board" viewBox="0 0 750 750" role="img" aria-label="The Harbour Collection For Sale board for Harbour Lane Estates">
    <rect width="750" height="750" fill="var(--board-white)"/>
    <path class="board-band" d="M0,0 H750 V198 C700,262 630,305 525,290 C410,272 300,178 160,192 C95,199 45,222 0,246 Z"/>
    <path class="band-edge" d="M750,198 C700,262 630,305 525,290 C410,272 300,178 160,192 C95,199 45,222 0,246"/>
    <rect class="board-frame" x="12" y="12" width="726" height="726"/>

    <text class="board-headline" x="375" y="132" text-anchor="middle">FOR SALE</text>
    <text class="collection-name" x="375" y="180" text-anchor="middle">THE HARBOUR COLLECTION</text>

    <rect class="brand-square" x="315" y="305" width="120" height="120"/>
    <text class="brand-name" x="375" y="520" text-anchor="middle">Harbour Lane Estates</text>

    <rect class="phone-pill" x="100" y="562" width="550" height="74" rx="37"/>
    <circle class="phone-badge" cx="137" cy="599" r="24"/>
    <path class="phone-handset" d="M127,587 l6,-3 l5,9 l-4,3 c1,4 4,7 8,9 l3,-4 l9,5 l-3,6 c-12,1 -25,-12 -24,-25 z"/>
    <text class="phone-number" x="395" y="620" text-anchor="middle">01632 960412</text>

    <text class="web-address" x="375" y="692" text-anchor="middle">www.<tspan class="web-domain">harbourlaneestates</tspan>.co.uk</text>
  </svg>
</main>
</body>
</html>
```